DOG DAYCARE BILLBOARD

Design a bold exciting billboard that can be read easily from a distance! Our goal is brand awareness and showcasing the services we offer (Boarding, Grooming, Daycare, and Training.
we would like to see examples with the phrase "your best friend's best day". Our name Bright Meadow Canine Activity Center (or just Bright Meadow might work better and could be bigger) and the services we provide.
(there are two examples of what we like included in the pictures)
you can find more information o our website at pawplayhub@mailnest.example.

```html
<!DOCTYPE html>
<html lang="en">
<head>
<meta charset="utf-8">
<title>Bright Meadow Billboard</title>
<link rel="stylesheet" href="https://fonts.googleapis.com/css2?family=Poppins:wght@600;700&family=Oswald:wght@500&display=swap">
<style>
  :root {
    --paper: #ffffff;
    --ink: #141414;
    --olive: #a59a2b;
    --olive-quote: #c3b92c;
    --mustard: #c8bd2f;
    --lime: #d3e12b;
    --band: #6e6428;
    --band-text: #ffffff;
  }
  html, body {
    margin: 0;
    padding: 0;
    width: 1200px;
    height: 1000px;
    overflow: hidden;
    background: var(--paper);
  }
  .billboard {
    position: relative;
    width: 1200px;
    height: 1000px;
    font-family: "Poppins", sans-serif;
    color: var(--ink);
  }
  .billboard__shapes {
    position: absolute;
    inset: 0;
  }
  .headline { position: absolute; margin: 0; font-weight: 700; line-height: 1; letter-spacing: -0.5px; white-space: nowrap; }
  .headline--your-best { left: 200px; top: 410px; font-size: 50px; color: var(--ink); }
  .headline--friends { left: 124px; top: 466px; font-size: 84px; color: var(--olive); font-weight: 600; }
  .headline--best { left: 122px; top: 545px; font-size: 50px; color: var(--ink); }
  .headline--day { left: 246px; top: 548px; font-size: 112px; color: var(--olive); font-weight: 600; }
  .quote-mark {
    position: absolute;
    font-family: "Poppins", sans-serif;
    font-weight: 700;
    font-size: 110px;
    line-height: 1;
    color: var(--olive-quote);
  }
  .quote-mark--open { left: 86px; top: 395px; }
  .quote-mark--close { left: 500px; top: 540px; }
  .brand {
    position: absolute;
    left: 96px;
    top: 690px;
    display: flex;
    align-items: center;
    gap: 14px;
  }
  .brand__dot {
    width: 26px;
    height: 26px;
    border-radius: 50%;
    background: var(--olive);
  }
  .brand__name {
    font-family: "Poppins", sans-serif;
    font-weight: 700;
    font-size: 40px;
    color: var(--ink);
    letter-spacing: -0.5px;
    white-space: nowrap;
  }
  .hero-dog {
    position: absolute;
    left: 600px;
    top: 166px;
    width: 380px;
    height: 510px;
    border-radius: 46% 40% 30% 34% / 30% 40% 26% 40%;
    background: radial-gradient(ellipse at 40% 45%, #c98a4a 0%, #a9713c 40%, #3d2d22 70%, #efe7dc 100%);
  }
  .service-band {
    position: absolute;
    left: 500px;
    top: 740px;
    width: 657px;
    height: 90px;
    box-sizing: border-box;
    padding: 0 28px;
    background: var(--band);
    border-radius: 16px 0 0 0;
    display: flex;
    align-items: center;
    justify-content: center;
  }
  .service-band__list {
    margin: 0;
    font-family: "Oswald", sans-serif;
    font-weight: 500;
    font-size: 30px;
    letter-spacing: 0.3px;
    color: var(--band-text);
    text-transform: uppercase;
    white-space: nowrap;
  }
</style>
</head>
<body>
<main class="billboard">
  <svg class="billboard__shapes" width="1200" height="1000" viewBox="0 0 1200 1000" aria-hidden="true">
    <defs>
      <clipPath id="panel-clip">
        <rect x="0" y="331" width="1157" height="669"/>
      </clipPath>
    </defs>
    <g clip-path="url(#panel-clip)">
      <circle class="accent-disc" cx="951" cy="471" r="190" fill="var(--mustard)"/>
      <circle class="accent-arc" cx="951" cy="520" r="255" fill="none" stroke="var(--lime)" stroke-width="2"/>
    </g>
  </svg>

  <div class="hero-dog" role="img" aria-label="Photo of a tricolour beagle in a playful bow, tail up"></div>

  <svg class="billboard__shapes" width="1200" height="1000" viewBox="0 0 1200 1000">
    <defs>
      <radialGradient id="ballpit" cx="0.55" cy="0.4" r="0.7">
        <stop offset="0" stop-color="#6b8ad6"/>
        <stop offset="0.45" stop-color="#c04a7a"/>
        <stop offset="0.75" stop-color="#8a5a32"/>
        <stop offset="1" stop-color="#5c9a4a"/>
      </radialGradient>
    </defs>
    <circle cx="1030" cy="600" r="124" fill="var(--lime)"/>
    <circle cx="1030" cy="600" r="115" fill="var(--paper)"/>
    <circle cx="1030" cy="600" r="110" fill="url(#ballpit)" role="img" aria-label="Photo of a dog playing in a pool of colourful balls"/>
  </svg>

  <span class="quote-mark quote-mark--open">“</span>
  <h1 class="headline headline--your-best">your best</h1>
  <p class="headline headline--friends">friend's</p>
  <p class="headline headline--best">best</p>
  <p class="headline headline--day">day</p>
  <span class="quote-mark quote-mark--close">”</span>

  <div class="brand">
    <span class="brand__dot"></span>
    <span class="brand__name">Bright Meadow</span>
  </div>

  <div class="service-band">
    <p class="service-band__list">Boarding / Grooming / Daycare / Training</p>
  </div>
</main>
</body>
</html>
```